Corlith Australia Pty Ltd

I require professional business cards with our company logo. We would like something that looks sharp and unique. I have attached the logo for our business, which is an industrial electrical contracting company. But this does not need to be shown on the cards.

Requirements
Must have
• The design must be double sided and needs to have one side with our logo only and the other side with our details.
Should not have
• We do not want any lightening bolts on the designs as this is very common.

```html
<!DOCTYPE html>
<html lang="en">
<head>
<meta charset="utf-8">
<title>Corlith Australia Pty Ltd — Business Cards</title>
<link href="https://fonts.googleapis.com/css2?family=Open+Sans:wght@400;600;700&display=swap" rel="stylesheet">
<style>
  :root {
    --backdrop-light: #b9b9b9;
    --backdrop-dark: #3d3d3d;
    --card-white: #ffffff;
    --gold: #c98f2c;
    --gold-deep: #a8721f;
    --gold-bright: #f0a94a;
    --gold-pale: #f6e79a;
    --ink: #111111;
  }
  * { box-sizing: border-box; margin: 0; padding: 0; }
  html, body { width: 1200px; height: 900px; overflow: hidden; }
  body {
    background: linear-gradient(120deg, var(--backdrop-light) 0%, #8d8d8d 55%, var(--backdrop-dark) 100%);
    font-family: "Open Sans", Arial, sans-serif;
    position: relative;
  }
  .card {
    position: absolute;
    width: 560px;
    height: 320px;
    background: var(--card-white);
    overflow: hidden;
    box-shadow: 0 10px 28px rgba(0,0,0,0.35);
  }
  .card-front { left: 90px; top: 90px; }
  .card-back { left: 550px; top: 490px; }

  .gold-field {
    position: absolute;
    background: linear-gradient(160deg, var(--gold-bright) 0%, var(--gold) 55%, var(--gold-deep) 100%);
  }
  .card-front .gold-field { top: 0; bottom: 0; width: 80px; }
  .card-front .gold-field-left { left: 0; }
  .card-front .gold-field-right { right: 0; }
  .card-back .gold-field { left: 0; right: 0; bottom: 0; height: 62px; }

  .brand { position: absolute; display: flex; align-items: center; color: var(--gold); font-weight: 700; }
  .brand-mark {
    border-radius: 50%;
    border: 6px solid var(--gold);
    flex: none;
  }
  .brand-text { line-height: 1; }
  .brand-name { display: block; letter-spacing: 0.04em; }
  .brand-sub { display: block; letter-spacing: 0.42em; }

  .card-front .brand { left: 80px; right: 80px; top: 62px; flex-direction: column; }
  .card-front .brand-mark { width: 82px; height: 82px; margin-bottom: 22px; }
  .card-front .brand-text { text-align: center; }
  .card-front .brand-name { font-size: 52px; }
  .card-front .brand-sub { font-size: 17px; margin-top: 6px; padding-left: 0.42em; }

  .card-back .brand { left: 150px; top: 26px; }
  .card-back .brand-mark { width: 64px; height: 64px; border-width: 5px; margin-right: 14px; }
  .card-back .brand-name { font-size: 40px; }
  .card-back .brand-sub { font-size: 13px; margin-top: 4px; }

  .contact { position: absolute; left: 196px; top: 118px; color: var(--ink); font-size: 12.5px; line-height: 1.42; }
  .contact-name { color: var(--gold); font-weight: 700; font-size: 14px; letter-spacing: 0.06em; margin-bottom: 2px; }
  .contact-role { color: var(--ink); font-weight: 400; font-size: 12.5px; letter-spacing: 0; margin-left: 4px; }
  .contact-label { font-weight: 700; }
  .contact-address { font-weight: 700; margin-top: 10px; }
</style>
</head>
<body>

<section class="card card-front" aria-label="Card front">
  <div class="gold-field gold-field-left" role="img" aria-label="Gold decorative border"></div>
  <div class="gold-field gold-field-right" role="img" aria-label="Gold decorative border"></div>
  <div class="brand">
    <span class="brand-mark"></span>
    <span class="brand-text">
      <span class="brand-name">CORLITH</span>
      <span class="brand-sub">AUSTRALIA PTY LTD</span>
    </span>
  </div>
</section>

<section class="card card-back" aria-label="Card back">
  <div class="gold-field" role="img" aria-label="Gold decorative band"></div>
  <div class="brand">
    <span class="brand-mark"></span>
    <span class="brand-text">
      <span class="brand-name">CORLITH</span>
      <span class="brand-sub">AUSTRALIA PTY LTD</span>
    </span>
  </div>
  <div class="contact">
    <p class="contact-name">MARCUS HALE<span class="contact-role">Director</span></p>
    <p><span class="contact-label">P:</span> 02 4719 3058 &nbsp;-&nbsp; <span class="contact-label">M:</span> 0438 216 947</p>
    <p>marcus@corlithaustralia.com.au</p>
    <p>www.corlithaustralia.com.au</p>
    <p class="contact-address">PO BOX 318, WESTMERE NSW 2590</p>
  </div>
</section>

</body>
</html>
```